INTERNATIONAL SHIPPING FOR THE MOVIE INDUSTRY

I have a new Freight forwarding/ Shipping company specialising in the movie industry, moving Movie cameras/sets doing the documentation for export & import to where ever the cargo goes world wide. I want clients to see that we are professionals as well as cost effective, e-tracking services available online like parcora/KVB
Services offered Air Exports/ Air Imports / Ocean Freight Import/Export, Customs clearances , trucking services, out of hours contacts, online tracking.. my company website www.morvell-hexaport.com

Target Market(s)

GENERAL PEOPLE LOOKING TO SHIP CARGO

Industry/Entity Type

Movie

Requirements
Must have
• INFORMATION ON MY PRODUCTS -
Intl Air Freight Forwarding - Priority/General/Deferred
Customs Brokerage -
Documentation Preparation - ATA Carnets / Nafta/ CofO
Packing and Crating
Pickup & Deliveries
Door to Door courier Service
Insurance & Bonding
Online Tracking
Nice to have
• i WANT IT TO BE EYE CATCHING AND PROFESSIONAL MAKING THE COMPANY LOOK BIG ENOUGH TO COPE AND SMALL ENOUGH TO CARE

```html
<!DOCTYPE html>
<html lang="en">
<head>
<meta charset="utf-8">
<title>Morvell – International Shipping for the Movie Industry</title>
<link href="https://fonts.googleapis.com/css2?family=Source+Sans+3:wght@400;600;700&family=Open+Sans:wght@400;600;700&display=swap" rel="stylesheet">
<style>
  :root{
    --page:#ffffff;
    --edge:#9a9a9a;
    --panel:#c0c0c0;
    --ink:#3a3a3a;
    --ink-soft:#454545;
    --heading:#3d3d3d;
    --accent:#4a4a4a;
  }
  *{margin:0;padding:0;box-sizing:border-box;}
  html,body{width:849px;height:1200px;overflow:hidden;background:var(--page);}
  .sheet{position:relative;width:849px;height:1200px;border:1px solid var(--edge);overflow:hidden;
    font-family:"Source Sans 3",sans-serif;color:var(--ink);}
  .block{position:absolute;}
  .panel{background:var(--panel);}

  .photo-bridge{background:
      linear-gradient(180deg,rgba(0,0,0,0) 0%,rgba(0,0,0,0) 70%,rgba(90,80,55,.35) 100%),
      linear-gradient(180deg,#54585f 0%,#6b6d71 12%,#8a4a36 13%,#7b4534 22%,#3f5a55 24%,#2f302e 34%,#3a3934 55%,#8f8466 72%,#7d6e50 88%,#4a4636 100%);}
  .photo-bridge-strip{background:linear-gradient(180deg,#6e7076 0%,#3b3a35 30%,#4a4840 55%,#a89570 80%,#7f7150 100%);}
  .photo-shelves{background:linear-gradient(180deg,#9c9488 0%,#b8ad9c 14%,#a33c22 24%,#8e3a24 30%,#3a342f 40%,#4b4036 65%,#5e4c3a 100%);}
  .photo-shelves-strip{background:linear-gradient(180deg,#c2a57c 0%,#a7865e 40%,#a24a2c 55%,#6a5440 70%,#8d7258 100%);}
  .photo-aisle{background:linear-gradient(180deg,#d5cfc2 0%,#bda27c 20%,#9c8062 45%,#6f655c 62%,#bdbab2 80%,#d6d4cd 100%);}

  .masthead{left:0;top:0;width:578px;height:180px;padding:44px 0 0 90px;color:var(--accent);}
  .masthead .brand{font-family:"Open Sans",sans-serif;font-size:30px;font-weight:700;letter-spacing:1px;color:#ffffff;}
  .masthead .brand::before{content:"";display:inline-block;width:18px;height:18px;background:#ffffff;margin-right:12px;vertical-align:2px;}
  .masthead .tagline{font-family:"Open Sans",sans-serif;font-size:15px;font-weight:600;letter-spacing:2px;text-transform:uppercase;margin-top:10px;}
  .masthead .sub{font-size:14px;margin-top:6px;}

  .domestic{left:90px;top:260px;width:386px;}
  .domestic h2{font-size:18px;font-weight:700;color:var(--heading);margin-bottom:14px;}
  .domestic p{font-size:14px;line-height:16.8px;text-align:justify;margin-bottom:16px;}
  .domestic h3{font-size:14px;font-weight:700;margin-bottom:16px;}
  .service-list{list-style:none;font-size:14px;line-height:16.8px;margin-bottom:16px;}
  .service-list li{position:relative;padding-left:16px;}
  .service-list li::before{content:"•";position:absolute;left:1px;}

  .key-features{left:594px;top:562px;width:255px;height:189px;padding:30px 0 0 15px;font-family:"Open Sans",sans-serif;}
  .key-features h2{font-size:16px;font-weight:600;color:var(--heading);margin-bottom:10px;}
  .key-features li{list-style:none;font-size:13.3px;line-height:16.8px;}

  .air-ocean{left:242px;top:768px;width:260px;height:287px;padding:23px 10px 0 15px;font-family:"Open Sans",sans-serif;}
  .air-ocean h2{font-size:16px;font-weight:600;color:var(--heading);margin-bottom:10px;}
  .air-ocean p{font-size:13.3px;line-height:16.8px;margin-bottom:16px;}
  .air-ocean .service-list{font-size:13.3px;padding-left:16px;}

  .contact{left:242px;top:1068px;font-family:"Open Sans",sans-serif;font-weight:700;font-size:12.8px;
    line-height:19px;color:var(--ink-soft);letter-spacing:.4px;font-style:normal;}
  .contact .phone{font-size:15.5px;}
</style>
</head>
<body>
<div class="sheet">
  <header class="block panel masthead">
    <div class="brand">MORVELL</div>
    <div class="tagline">International Shipping for the Movie Industry</div>
    <div class="sub">Cameras, sets &amp; production cargo – moved and documented worldwide.</div>
  </header>
  <div class="block photo-bridge" role="img" aria-label="Stacked freight containers on a train crossing a steel trestle bridge" style="left:594px;top:0;width:255px;height:544px;"></div>
  <div class="block photo-bridge-strip" role="img" aria-label="Detail of the steel trestle bridge over dry grassland" style="left:515px;top:193px;width:63px;height:351px;"></div>

  <section class="block domestic">
    <h2>Domestic Freight / 3 PL Warehousing</h2>
    <p>Our warehousing and fulfillment solutions allow you to have your products ready to move, locally, domestically or internationally as you require, when you require. Our team continually strives to help build you a strong network.</p>
    <h3>Domestic Solutions</h3>
    <ul class="service-list">
      <li>Air Freight</li>
      <li>&nbsp;Local/ Nationwide Collections &amp; Deliveries</li>
      <li>Nationwide Drayage Service</li>
      <li>Expedited Road Transport (50 States)</li>
      <li>Team Drivers</li>
      <li>Canadian Cross Border Trucking</li>
      <li>Border Clearances</li>
    </ul>
    <h3>3PL Warehousing &amp; Distribution</h3>
    <ul class="service-list">
      <li>Contract Warehousing</li>
      <li>Fulfillment / Pick &amp; Pack</li>
      <li>Container Devanning &amp; Loading</li>
      <li>Managed Inventory &amp; Rotation</li>
      <li>Professional Packing</li>
      <li>Bonded Warehousing available</li>
    </ul>
  </section>

  <div class="block panel" style="left:515px;top:562px;width:65px;height:95px;"></div>
  <section class="block panel key-features">
    <h2>Our Key features:</h2>
    <ul>
      <li>ATA Carnets / NAFTA / CofO</li>
      <li>Packing and Crating</li>
      <li>Pickup &amp; Deliveries</li>
      <li>Door to Door courier Service</li>
      <li>Insurance &amp; Bonding</li>
      <li>Online Tracking</li>
    </ul>
  </section>

  <div class="block photo-shelves" role="img" aria-label="Warehouse pallet racking with labelled shelf bays and boxed goods" style="left:0;top:768px;width:227px;height:353px;"></div>
  <section class="block panel air-ocean">
    <h2>Air Freight / Ocean Freight</h2>
    <p>Morvell provides International Airfreight to and from all major airport of the world. Our air cargo team members can take you through the booking process from collection to delivery ensuring all criteria are met.</p>
    <ul class="service-list">
      <li>Primary Air Freight Services</li>
      <li>Primary Ocean Cargo Services</li>
      <li>Specialized Services</li>
      <li>Customs Brokerage</li>
    </ul>
  </section>
  <div class="block photo-shelves-strip" role="img" aria-label="Stacked cardboard cartons on warehouse racking" style="left:515px;top:768px;width:63px;height:287px;"></div>
  <div class="block photo-aisle" role="img" aria-label="Warehouse aisle with tall racking of wrapped pallets and a yellow floor line" style="left:594px;top:768px;width:255px;height:351px;"></div>

  <address class="block contact">
    Need help?<br>
    Call us toll free <span class="phone">1-888-555-0147</span><br>
    Email Us: Info@morvell-hexaport.com
  </address>
</div>
</body>
</html>
```